Dental Office Looking for Modern, simple business cards

We just acquired our logo. Now we would like to make business cards. We are a dental office with two doctors. We are husband and wife and have a small boutique dental practice in a small town. We love our patients and they are always asking us to give our business cards to their friends. Please help us make business cards :-)

Target Market(s)

30-60 yr old

Industry/Entity Type

Dental Clinic

Contact Information for Business Card

Birch Hollow Dental P.C.
Family and Cosmetic Dentistry
4826 Delmore Rd. Schenectady NY 12417
Tel: 518 642 7731 Fax: 518 642 7048

Dr. Tomas K. Brellin DDS
Dr. Marisol Ede Thornquist DDS

Font styles to use
Serif
Sans Serif

Requirements
Must have
• Simple clean design, modern, colorful. Should incorporate the logo.
Nice to have
• dental imagery ( teeth, smile, etc ...).

```html
<!DOCTYPE html>
<html lang="en">
<head>
<meta charset="utf-8">
<title>Birch Hollow Dental – Business Card</title>
<link href="https://fonts.googleapis.com/css2?family=Cinzel:wght@500&family=Poppins:wght@400;600&display=swap" rel="stylesheet">
<style>
  :root {
    --backdrop: #163a60;
    --brand-blue: #1f7ec4;
    --card-white: #ffffff;
    --ink-grey: #7a7f86;
    --accent-grey: #8a8c90;
    --shadow: rgba(5, 20, 40, 0.45);
  }
  * { box-sizing: border-box; margin: 0; padding: 0; }
  html, body {
    width: 1200px; height: 900px; overflow: hidden;
    background: var(--backdrop);
  }
  .stage { position: relative; width: 1200px; height: 900px; }
  .card {
    position: absolute; width: 560px; height: 320px;
    border-radius: 28px; overflow: hidden;
    box-shadow: 0 14px 30px var(--shadow);
  }
  .card--front {
    left: 320px; top: 100px;
    background: var(--brand-blue);
    display: flex; align-items: center; justify-content: center;
  }
  .wordmark {
    font-family: "Cinzel", serif; font-weight: 500;
    color: var(--card-white); font-size: 40px; letter-spacing: 2px;
    text-align: center; line-height: 1.1;
  }
  .card--back {
    left: 320px; top: 480px;
    background: var(--card-white);
  }
  .brand-decoration {
    position: absolute; left: 0; top: 0; width: 250px; height: 320px;
    background: linear-gradient(135deg, #d9e9f6 0%, #9cc6e6 55%, #c9cbcf 100%);
  }
  .contact {
    position: absolute; left: 282px; top: 58px; right: 24px;
    font-family: "Poppins", sans-serif; color: var(--ink-grey);
  }
  .contact__name {
    color: var(--brand-blue); font-weight: 600; font-size: 19px; line-height: 1.2;
  }
  .contact__title { font-size: 11px; margin-bottom: 14px; letter-spacing: 0.3px; }
  .contact__list { list-style: none; font-size: 11px; line-height: 1.9; }
  .contact__list li { display: flex; align-items: center; gap: 9px; }
  .contact__list svg { width: 12px; height: 12px; flex: none; }
  .contact__address { margin-top: 12px; font-size: 11px; line-height: 1.6; }
</style>
</head>
<body>
<main class="stage">
  <section class="card card--front">
    <p class="wordmark">Birch Hollow Dental</p>
  </section>

  <section class="card card--back">
    <div class="brand-decoration" role="img" aria-label="Large brand mark decoration area in blue and grey"></div>
    <div class="contact">
      <h1 class="contact__name">Dr. Tomas K. Brellin DDS</h1>
      <p class="contact__title">Managing Director</p>
      <ul class="contact__list">
        <li>
          <svg viewBox="0 0 12 12" fill="var(--brand-blue)"><path d="M2.5 0.8l2 2-1.2 1.4a7 7 0 0 0 4.5 4.5L9.2 7.5l2 2-1.5 1.7C5.5 11 1 6.5 0.8 2.3z"/></svg>
          518 642 7731
        </li>
        <li>
          <svg viewBox="0 0 12 12" fill="var(--brand-blue)"><rect x="3" y="0.5" width="6" height="4"/><rect x="0.5" y="4.5" width="11" height="5" rx="1"/><rect x="3" y="8" width="6" height="3.5" fill="#fff" stroke="var(--brand-blue)"/></svg>
          518 642 7048
        </li>
        <li>
          <svg viewBox="0 0 12 12" fill="none" stroke="var(--brand-blue)" stroke-width="1.2"><rect x="0.8" y="2" width="10.4" height="8" rx="1"/><path d="M1 2.5l5 4 5-4"/></svg>
          tomas@birchhollowdental.com
        </li>
        <li>
          <svg viewBox="0 0 12 12" fill="none" stroke="var(--brand-blue)" stroke-width="1.2"><circle cx="6" cy="6" r="5"/><path d="M1 6h10M6 1c-2.5 3-2.5 7 0 10M6 1c2.5 3 2.5 7 0 10"/></svg>
          www.birchhollowdental.com
        </li>
      </ul>
      <p class="contact__address">Family and Cosmetic Dentistry<br>4826 Delmore Rd. Schenectady NY 12417</p>
    </div>
  </section>
</main>
</body>
</html>
```